Brighter Than Dawn Home Entertainment

We are a home theater installation company focus on front projection system and home theater surround system. We built highend home theater for people to enjoy movie, sports and gaming on big screen at home.
I'm looking for a dispaly to showcase our work as well as help people build their home theater

Number of Pages Required

3 page

Colors

Designer to choose colors to be used in the design.

Requirements
Must have
• Home Page
• What we do
• Who we are
• Gallery
• Contact Us
Nice to have
• Picture jump out of big screen make a 3D feeling

```html
<!DOCTYPE html>
<html lang="en">
<head>
<meta charset="utf-8">
<title>Brighter Than Dawn</title>
<link rel="stylesheet" href="https://fonts.googleapis.com/css2?family=Poppins:ital,wght@0,400;0,500;0,600;0,700;1,400&display=swap">
<style>
:root{
  --red:#e8173c;
  --ink:#1d1d1d;
  --body:#555;
  --light:#f7f7f7;
  --gray:#ececec;
  --black:#111;
  --deep:#050505;
  --white:#fff;
}
*{box-sizing:border-box;margin:0;padding:0}
html,body{width:1200px;height:3087px;overflow:hidden}
body{font-family:"Poppins",sans-serif;color:var(--ink);position:relative;background:var(--white)}
.abs{position:absolute}
section,header,footer{position:absolute;left:0;width:1200px;overflow:hidden}

/* hero */
.hero{top:0;height:600px}
.hero-bg{position:absolute;inset:0;background:radial-gradient(ellipse at 50% 40%,#5b5450 0%,#3b3633 45%,#1e1b1a 100%)}
.hero-floor{position:absolute;left:0;right:0;bottom:0;height:150px;background:linear-gradient(180deg,rgba(0,0,0,0),rgba(0,0,0,.55))}
.brand{left:100px;top:40px;font-size:30px;font-weight:700;color:var(--white)}
.topline{right:100px;top:12px;font-size:14px;color:var(--white);display:flex;align-items:center;gap:8px;font-weight:500}
.nav{right:100px;top:48px;display:flex;gap:33px;font-size:16px;font-weight:500;color:var(--white)}
.screen{left:425px;top:250px;width:360px;height:212px;border:10px solid #7a7672;background:#151515;display:flex;flex-direction:column;align-items:center;justify-content:center;color:var(--white)}
.screen .pre{font-size:21px;font-weight:500}
.screen .name{font-size:30px;font-weight:700;margin-top:4px;text-align:center;line-height:1.2}
.dots{left:162px;top:532px;display:flex;gap:8px;align-items:center}
.dots i{width:9px;height:9px;border-radius:50%;background:var(--white);display:block}
.dots i.on{width:16px;height:16px;border:2px solid var(--white);background:transparent;position:relative}
.dots i.on::after{content:"";position:absolute;left:3px;top:3px;width:6px;height:6px;border-radius:50%;background:var(--white)}
.tab{left:560px;top:578px}

/* section headings */
.kicker{width:1200px;text-align:center;font-size:11px;font-style:italic;color:#333}
.dash{left:588px;width:24px;height:3px;background:var(--red)}
.title{width:1200px;text-align:center;font-size:32px;font-weight:700;color:var(--red)}

/* what we do */
.what{top:600px;height:645px;background:var(--light)}
.what h3{left:100px;top:208px;width:450px;font-size:19px;font-weight:500;line-height:1.5;color:var(--ink)}
.what p{left:100px;top:282px;width:440px;font-size:14px;line-height:27.5px;color:var(--body)}
.btn{left:100px;top:499px;width:142px;height:39px;border-radius:20px;background:var(--red);color:var(--white);font-size:13px;font-weight:600;display:flex;align-items:center;justify-content:center}
.slide{position:absolute}
.s1{left:600px;top:243px;width:110px;height:256px;background:linear-gradient(180deg,#bfbfbf,#9a9a9a);opacity:.8}
.s2{left:704px;top:205px;width:262px;height:332px;background:linear-gradient(180deg,#0d1a3a,#1f3a78 55%,#0b1024)}
.s3{left:966px;top:222px;width:124px;height:302px;background:linear-gradient(180deg,#2a1b12,#6b4326 60%,#1a100a)}
.s4{left:1090px;top:243px;width:102px;height:258px;background:linear-gradient(180deg,#d9d9d9,#a8a8a8)}
.sdots{left:914px;top:505px;display:flex;gap:6px}
.sdots i{width:8px;height:8px;border-radius:50%;display:block;border:1.5px solid var(--white)}
.sdots i.on{background:var(--white)}

/* who we are */
.who{top:1245px;height:540px;background:var(--red);color:var(--white)}
.who .kicker,.who .title{color:var(--white)}
.who .dash{background:var(--white)}
.who .lead{left:200px;top:160px;width:800px;text-align:center;font-size:14px;line-height:27px}
.card{top:243px;height:187px}
.c1{left:100px;width:319px;background:linear-gradient(135deg,#e9e9e9,#b9b9b9 60%,#7a7570)}
.c2{left:441px;width:316px;background:#1c1c1c;display:flex;align-items:center;justify-content:center;text-align:center;font-size:15px;line-height:27px;padding:0 30px}
.c2 span{background:rgba(0,0,0,.4)}
.c3{left:784px;width:316px;background:linear-gradient(135deg,#7a2a2a,#3a4f78 55%,#2c2c44)}
.cap{top:452px;font-size:19px;font-weight:600}

/* gallery */
.gallery{top:1785px;height:493px;background:var(--gray)}
.gimg{position:absolute;top:218px;height:275px}
.g1{left:0;width:296px;background:linear-gradient(135deg,#caa393,#7a5a52 60%,#3a2a28)}
.g2{left:302px;width:296px;background:linear-gradient(180deg,#2f3a2a,#1a2636 55%,#101010)}
.g3{left:603px;width:296px;background:linear-gradient(180deg,#0a3a48,#0f6b7d 45%,#0b1a22)}
.g4{left:905px;width:295px;background:linear-gradient(135deg,#8a8fa0,#4a5a78 55%,#2a2f3a)}

/* testimonials */
.testi{top:2278px;height:474px;background:linear-gradient(180deg,#fbf3f4,#f7eff0)}
.quote{left:238px;top:198px;width:724px;text-align:center;font-size:15px;line-height:27px;color:#444}
.qm{font-size:70px;font-weight:700;color:#333;line-height:1}
.author{width:1200px;top:322px;text-align:center;font-size:19px;font-weight:500;color:#333}
.tdots{left:567px;top:408px;display:flex;gap:6px}
.tdots i{width:20px;height:4px;background:#333;display:block}
.tdots i.on{background:var(--red)}

/* footer */
.foot{top:2752px;height:273px;background:var(--black);color:var(--white)}
.foot h4{font-size:15px;font-weight:700;position:absolute;top:50px}
.foot .txt{position:absolute;font-size:13px;line-height:25px}
.links{top:90px;left:409px}
.social{left:100px;top:210px;display:flex;gap:12px}
.social i{width:10px;height:10px;border-radius:50%;background:var(--white);display:block}
.crow{position:absolute;left:584px;display:flex;gap:14px;align-items:flex-start;font-size:13px;line-height:23px}
.news{left:859px;top:100px;width:240px}
.field{left:859px;top:187px;width:197px;height:41px;background:var(--white);color:#888;font-size:11px;font-style:italic;padding:12px 13px}
.go{left:1056px;top:187px;width:43px;height:41px;background:var(--red);display:flex;align-items:center;justify-content:center}
.bar{top:3025px;height:62px;background:var(--deep);color:var(--white);font-size:13px;display:flex;align-items:center;justify-content:center}
</style>
</head>
<body>

<header class="hero">
  <div class="hero-bg" role="img" aria-label="Home theater room with shelves, speakers, leather recliners and a wall-mounted screen"></div>
  <div class="hero-floor"></div>
  <div class="abs brand">Brighter Than Dawn</div>
  <div class="abs topline">
    <svg width="14" height="14" viewBox="0 0 24 24" fill="#fff"><path d="M6.6 10.8a15.1 15.1 0 0 0 6.6 6.6l2.2-2.2c.3-.3.7-.4 1-.2 1.1.4 2.3.6 3.6.6.6 0 1 .4 1 1V20c0 .6-.4 1-1 1A17 17 0 0 1 3 4c0-.6.4-1 1-1h3.5c.6 0 1 .4 1 1 0 1.3.2 2.5.6 3.6.1.3 0 .7-.2 1z"/></svg>
    <span>+1 555 014 2290</span>
    <svg style="margin-left:34px" width="14" height="14" viewBox="0 0 24 24" fill="none" stroke="#fff" stroke-width="3"><circle cx="10" cy="10" r="7"/><path d="M15 15l6 6"/></svg>
  </div>
  <nav class="abs nav"><span>Home</span><span>What we do</span><span>Who we are</span><span>Gallery</span><span>Contact us</span></nav>
  <div class="abs screen"><div class="pre">Welcome To</div><div class="name">Brighter Than Dawn</div></div>
  <div class="abs dots"><i class="on"></i><i></i><i></i></div>
  <svg class="abs tab" width="80" height="22" viewBox="0 0 80 22"><path d="M0 22 L20 2 Q22 0 26 0 H54 Q58 0 60 2 L80 22Z" fill="#f7f7f7"/><path d="M34 7l6 6 6-6" stroke="#222" stroke-width="2.5" fill="none"/></svg>
</header>

<section class="what">
  <div class="abs kicker" style="top:72px">At vero eos et</div>
  <div class="abs dash" style="top:101px"></div>
  <h2 class="abs title" style="top:113px">What we do</h2>
  <h3 class="abs">But I must explain to you how all this mistaken idea of denouncing pleasure</h3>
  <p class="abs">At vero eos et accusamus et iusto odio dignissimos ducimus qui blanditiis praesentium voluptatum deleniti atque corrupti quos dolores et quas molestias excepturi sint occaecati cupiditate non provident, similique sunt in culpa qui officia deserunt mollitia animi, id est laborum et dolorum fuga. Et harum quidem rerum facilis est et expedita distinctio.</p>
  <div class="abs btn">READ MORE</div>
  <div class="slide s1" role="img" aria-label="Living room with wall screen"></div>
  <div class="slide s4" role="img" aria-label="Media wall with television"></div>
  <div class="slide s3" role="img" aria-label="Theater room with projection screen"></div>
  <div class="slide s2" role="img" aria-label="Private cinema with blue recliner seating"></div>
  <div class="abs sdots"><i class="on"></i><i></i></div>
</section>

<section class="who">
  <div class="abs kicker" style="top:60px">At vero eos et</div>
  <div class="abs dash" style="top:87px"></div>
  <h2 class="abs title" style="top:98px">Who we are</h2>
  <p class="abs lead">Sed ut perspiciatis unde omnis iste natus error sit voluptatem accusantium doloremque laudantium, totam rem aperiam, eaque ipsa quae ab illo inventore veritatis et quasi architecto beatae vitae</p>
  <div class="abs card c1" role="img" aria-label="Technician installing a tower speaker beside a television"></div>
  <svg class="abs" style="left:369px;top:258px" width="30" height="22" viewBox="0 0 30 22"><rect x="0" y="6" width="20" height="14" rx="2" fill="#e8173c"/><path d="M20 10l9-5v14l-9-5z" fill="#e8173c"/><circle cx="5" cy="3" r="3" fill="#e8173c"/><circle cx="13" cy="3" r="3" fill="#e8173c"/></svg>
  <div class="abs card c2"><span>But I must explain to you how all this mistaken idea of denouncing pleasure and praising pain was born</span></div>
  <div class="abs card c3" role="img" aria-label="Friends watching a film together on a sofa"></div>
  <svg class="abs" style="left:1040px;top:243px" width="60" height="60" viewBox="0 0 60 60"><path d="M0 0H60V60Z" fill="#fff"/><circle cx="44" cy="16" r="9" fill="#e8173c"/></svg>
  <div class="abs cap" style="left:198px">Installation</div>
  <div class="abs cap" style="left:474px">Services</div>
  <svg class="abs" style="left:713px;top:451px" width="28" height="28" viewBox="0 0 28 28"><circle cx="14" cy="14" r="14" fill="#fff"/><path d="M11 8l6 6-6 6" stroke="#e8173c" stroke-width="3" fill="none"/></svg>
  <div class="abs cap" style="left:900px">Support</div>
</section>

<section class="gallery">
  <div class="abs kicker" style="top:62px">At vero eos et</div>
  <div class="abs dash" style="top:90px"></div>
  <h2 class="abs title" style="top:102px">Gallery</h2>
  <div class="gimg g1" role="img" aria-label="Couple relaxing on a sofa"></div>
  <div class="gimg g2" role="img" aria-label="Family watching a game on a big screen"></div>
  <div class="gimg g3" role="img" aria-label="Viewers in front of a glowing screen"></div>
  <div class="gimg g4" role="img" aria-label="Friends laughing on a couch with popcorn"></div>
</section>

<section class="testi" role="group" aria-label="Testimonials">
  <div class="abs kicker" style="top:68px">At vero eos et</div>
  <div class="abs dash" style="top:97px"></div>
  <h2 class="abs title" style="top:108px">Testimonials</h2>
  <div class="abs qm" style="left:188px;top:175px">&ldquo;</div>
  <p class="abs quote">Sed ut perspiciatis unde omnis iste natus error sit voluptatem accusantium doloremque laudantium, totam rem aperiam, eaque ipsa quae ab illo inventore veritatis et quasi architecto beatae vitae dicta sunt explicabo.</p>
  <div class="abs qm" style="left:978px;top:228px">&rdquo;</div>
  <div class="abs author">- Maren</div>
  <div class="abs tdots"><i class="on"></i><i></i><i></i></div>
</section>

<footer class="foot">
  <h4 style="left:100px">ABOUT US</h4>
  <p class="txt" style="left:100px;top:90px;width:250px">Lorem ipsum dolor sit amet, consectetur adipiscing elit, sed do eiusmod tempor incididunt ut labore et dolore magna aliqua.</p>
  <div class="abs social"><i></i><i></i><i></i><i></i></div>

  <h4 style="left:409px">LINKS</h4>
  <div class="txt links" style="line-height:27px">Home<br>What we do<br>Who we are<br>Gallery<br>Contact us</div>

  <h4 style="left:584px">CONTACT US</h4>
  <div class="crow" style="top:88px"><svg width="16" height="18" viewBox="0 0 16 18" fill="none" stroke="#fff" stroke-width="1.5"><path d="M8 1a5 5 0 0 1 5 5c0 4-5 9-5 9S3 10 3 6a5 5 0 0 1 5-5z"/><circle cx="8" cy="6" r="2"/></svg><span># 42, 7 Harbor Lane,<br>Coral Bay FL 3301</span></div>
  <div class="crow" style="top:154px"><svg width="16" height="16" viewBox="0 0 24 24" fill="#fff"><path d="M6.6 10.8a15.1 15.1 0 0 0 6.6 6.6l2.2-2.2c.3-.3.7-.4 1-.2 1.1.4 2.3.6 3.6.6.6 0 1 .4 1 1V20c0 .6-.4 1-1 1A17 17 0 0 1 3 4c0-.6.4-1 1-1h3.5c.6 0 1 .4 1 1 0 1.3.2 2.5.6 3.6.1.3 0 .7-.2 1z"/></svg><span>+1 555 014 2290</span></div>
  <div class="crow" style="top:200px"><svg width="16" height="14" viewBox="0 0 16 12" fill="#fff"><path d="M0 0h16v12H0z"/><path d="M0 0l8 6 8-6" stroke="#111" stroke-width="1.3" fill="none"/></svg><span>hello@brighterthandawn.com</span></div>

  <h4 style="left:859px">NEWSLETTER</h4>
  <p class="txt news">But I must explain to you how all this mistaken idea of denouncing pleasure and praising.</p>
  <div class="abs field">Enter your email address</div>
  <div class="abs go"><svg width="14" height="12" viewBox="0 0 14 12"><path d="M0 6h11M7 1l5 5-5 5" stroke="#fff" stroke-width="2" fill="none"/></svg></div>
</footer>

<div class="abs bar" style="left:0;width:1200px">© 2018 Brighter Than Dawn | All Rights Reserved</div>

</body>
</html>
```